Melissa Dorvan Personal Business Card

I like orange. It's would better if my card have an orange background
Address: 5820 Halvers Lane #417
San Jose
California
US
Tel: 4085172049

Industry/Entity Type

Business

```html
<!DOCTYPE html>
<html lang="en">
<head>
<meta charset="utf-8">
<title>Melissa Dorvan — Business Card</title>
<link rel="stylesheet" href="https://fonts.googleapis.com/css2?family=Della+Respira&family=Cormorant+Garamond:ital,wght@1,500&display=swap">
<style>
  :root {
    --page: #f4f1ee;
    --card-deep: #c4481a;
    --card-mid: #d9622a;
    --card-light: #e57a35;
    --band: #f0782a;
    --ornament: #b23c1e;
    --ink: #ffffff;
  }
  html, body {
    margin: 0;
    width: 1200px;
    height: 855px;
    overflow: hidden;
    background: var(--page);
  }
  .canvas {
    position: relative;
    width: 1200px;
    height: 855px;
  }
  .card {
    position: absolute;
    left: 100px;
    top: 140px;
    width: 1000px;
    height: 575px;
    border-radius: 34px;
    overflow: hidden;
    background: radial-gradient(ellipse at 55% 45%, var(--card-light) 0%, var(--card-mid) 45%, var(--card-deep) 100%);
  }
  .card__band {
    position: absolute;
    left: 760px;
    top: 0;
    width: 80px;
    height: 100%;
    background: var(--band);
  }
  .card__ornament {
    position: absolute;
    left: 610px;
    top: 190px;
    width: 300px;
    height: 385px;
    border-radius: 150px 150px 0 0;
    background: linear-gradient(180deg, rgba(178, 60, 30, 0) 0%, rgba(178, 60, 30, 0.45) 40%, rgba(178, 60, 30, 0.6) 100%);
  }
  .card__rules {
    position: absolute;
    inset: 0;
  }
  .card__name {
    position: absolute;
    left: 58px;
    top: 30px;
    margin: 0;
    font-family: "Della Respira", serif;
    font-weight: 400;
    font-size: 70px;
    line-height: 1;
    color: var(--ink);
    letter-spacing: 1px;
  }
  .card__contact {
    position: absolute;
    left: 62px;
    top: 292px;
    margin: 0;
    font-family: "Cormorant Garamond", serif;
    font-style: italic;
    font-weight: 500;
    font-size: 31px;
    line-height: 45px;
    color: var(--ink);
  }
  .card__contact span { display: block; }
</style>
</head>
<body>
<main class="canvas">
  <section class="card" aria-label="Business card of Melissa Dorvan">
    <div class="card__band"></div>
    <div class="card__ornament" role="img" aria-label="Floral swirl ornament rising along the right band"></div>
    <svg class="card__rules" width="1000" height="575" viewBox="0 0 1000 575" aria-hidden="true">
      <polyline points="318,92 318,126 1000,126" fill="none" stroke="#ffffff" stroke-width="2.5"/>
      <polyline points="0,262 430,262 430,575" fill="none" stroke="#ffffff" stroke-width="2.5"/>
    </svg>
    <h1 class="card__name">Melissa Dorvan</h1>
    <address class="card__contact">
      <span>5820 Halvers Lane #417</span>
      <span>San Jose</span>
      <span>California</span>
      <span>US</span>
      <span>4085172049</span>
    </address>
  </section>
</main>
</body>
</html>
```